Investment website design - investing in mutual funds

I need a design of a website (only homepage for now) dedicated to investment in mutual funds. Attached is a mock up with all the elements the homepage design should contain. The homepage should contain a logo in the upper left corner, the domain the website will run on is www.morvatelsko.cz , in the upper right corner there should be 2 buttons or links SIGN UP / SIGN IN. The bottom of the homepage should contain links to ABOUT US, FAQ, PRIVACY POLICY, CONTACT US.
Now the main elements on the homepage
1) Video that will explain how the investment works exactly, under this video we will have 3 illustrated icons like the ones attached (see 2nd attachement) that will show the potential investor what exactly they could get when investing with us (education for kids, happy life after they retire, regular monthly payment for the rest of their life).
2) On the right side next to the video we will have a calculator where a potential investor can play with the numbers, the investor can fill in the MONTHLY PAYMENT that he wants to invest regularly every month, the time frame of the investment - for how long he wants to invest. Once the potential investor selects those 2 variables we will calculate for him 2 options - either he can get a ONE TIME PAYOUT once he reaches his investment horizon or he can get a regular monthly payment for the rest of his life. Under the laculator there will be a button 'I want to invest ->'. The functionality of the calculator should be similar to the calculator that can be found here http://www.brovikbanka.cz/brovik-podilove-fondy/ and https://pelvaro.cz/.
The design should look similar to https://pelvaro.cz/ (font, colors, logo). We prefer white background in the area where we have the video and calculator. We also like the design of www.truvanex.com. Let me know if you have any questions.

```html
<!DOCTYPE html>
<html lang="en">
<head>
<meta charset="utf-8">
<title>morvatelsko.cz – Investing in mutual funds</title>
<link rel="stylesheet" href="https://fonts.googleapis.com/css2?family=Roboto+Slab:wght@300;400;500;700&family=Roboto+Condensed:wght@700&display=swap">
<style>
  :root {
    --teal: #43b3be;
    --teal-dark: #3aa4ae;
    --orange: #e8583a;
    --ink: #1d1d1d;
    --grey: #7a7a7a;
    --circle: #e9e9e9;
    --white: #ffffff;
  }
  * { box-sizing: border-box; margin: 0; padding: 0; }
  html, body { width: 1200px; height: 590px; overflow: hidden; background: var(--white); }
  body { position: relative; font-family: "Roboto Slab", Georgia, serif; color: var(--ink); }

  .site-header {
    position: absolute; left: 0; top: 0; width: 1200px; height: 90px;
    background: var(--teal); box-shadow: 0 2px 4px rgba(0,0,0,.25);
  }
  .brand {
    position: absolute; left: 80px; top: 26px;
    font-size: 34px; font-weight: 700; color: var(--ink); letter-spacing: -0.5px;
  }
  .auth-btn {
    position: absolute; top: 30px; height: 30px;
    background: var(--orange); color: var(--white);
    font-size: 12px; display: flex; align-items: center; justify-content: center; gap: 6px;
    box-shadow: 1px 2px 3px rgba(0,0,0,.25); text-decoration: none;
  }
  .auth-btn.sign-in { left: 932px; width: 84px; }
  .auth-btn.sign-up { left: 1033px; width: 85px; }

  .video-tab {
    position: absolute; left: 0; top: 90px; width: 40px; height: 353px;
    background: var(--orange); color: var(--white);
    display: flex; flex-direction: column; align-items: center; padding-top: 10px;
    font-size: 13px; font-weight: 700; line-height: 13px;
  }
  .video-tab span { display: block; height: 13.1px; }
  .video-tab .gap { height: 6px; }
  .video-tab svg { margin-top: 6px; }

  .video {
    position: absolute; left: 40px; top: 90px; width: 547px; height: 353px;
    background: radial-gradient(ellipse at 45% 50%, #d9c3b4 0%, #bfe0e3 40%, #b3dfe3 100%);
  }
  .play {
    position: absolute; left: 276px; top: 234px; width: 62px; height: 62px;
    border-radius: 50%; background: var(--orange);
  }

  .benefits { position: absolute; left: 0; top: 470px; width: 587px; height: 100px; }
  .benefit { position: absolute; top: 0; width: 160px; text-align: center; }
  .benefit .art { width: 70px; height: 70px; border-radius: 50%; background: var(--circle); margin: 0 auto; }
  .benefit .label {
    margin-top: 16px; color: var(--orange);
    font-family: "Roboto Condensed", Arial, sans-serif; font-weight: 700; font-size: 14px;
  }
  .dash { position: absolute; top: 35px; width: 105px; border-top: 1px dashed var(--orange); }

  .calculator { position: absolute; left: 681px; top: 0; width: 430px; }
  .calc-title {
    position: absolute; left: 0; top: 124px; width: 430px;
    display: flex; align-items: center; gap: 12px;
    font-size: 21px; font-weight: 500; text-transform: uppercase;
  }
  .calc-title .badge {
    width: 31px; height: 31px; border-radius: 50%; background: var(--teal);
    display: flex; align-items: center; justify-content: center;
  }
  .field {
    position: absolute; left: 0; width: 430px; height: 54px;
    border: 1px solid var(--orange); display: flex; align-items: center;
    color: var(--orange); font-size: 13px; font-weight: 300;
  }
  .field svg { margin: 0 20px 0 19px; }
  .range-label { position: absolute; left: 0; top: 238px; font-size: 13px; font-weight: 300; }
  .range { position: absolute; left: 0; top: 258px; width: 430px; height: 50px; }
  .range .value {
    position: absolute; left: 0; top: 0; width: 15px; height: 15px; border-radius: 3px;
    background: var(--orange); color: var(--white); font-size: 10px; text-align: center; line-height: 15px;
  }
  .range .ends { position: absolute; top: 35px; font-size: 12px; font-weight: 700; color: var(--grey); }
  .invest-btn {
    position: absolute; left: 0; top: 443px; width: 430px; height: 54px;
    background: var(--orange); color: var(--white); font-size: 24px; font-weight: 400;
    display: flex; align-items: center; justify-content: center; gap: 12px; text-decoration: none;
  }

  .footer-nav { position: absolute; right: 39px; top: 546px; display: flex; }
  .footer-nav a {
    color: var(--teal); font-size: 13px; font-weight: 300; text-decoration: none;
    padding: 2px 16px; border-left: 1px solid #cfe9ec;
  }
  .footer-nav a:first-child { border-left: none; }
</style>
</head>
<body>

<header class="site-header">
  <div class="brand">morvatelsko.cz</div>
  <a class="auth-btn sign-in" href="#">
    <svg width="13" height="11" viewBox="0 0 13 11"><path d="M0 4h6V1l4 4.5L6 10V7H0z" fill="#fff"/><path d="M8 0h5v11H8V9.5h3.5v-8H8z" fill="#fff"/></svg>
    SIGN IN
  </a>
  <a class="auth-btn sign-up" href="#">
    <svg width="13" height="12" viewBox="0 0 13 12"><circle cx="6" cy="3.5" r="3.2" fill="#fff"/><path d="M0 12c0-4 2.5-5.5 6-5.5s6 1.5 6 5.5z" fill="#fff"/></svg>
    SIGN UP
  </a>
</header>

<div class="video-tab">
  <span>V</span><span>I</span><span>D</span><span>E</span><span>O</span><span class="gap"></span>
  <span>A</span><span>B</span><span>O</span><span>U</span><span>T</span><span class="gap"></span>
  <span>O</span><span>U</span><span>R</span><span class="gap"></span>
  <span>P</span><span>R</span><span>O</span><span>D</span><span>U</span><span>C</span><span>T</span>
  <svg width="28" height="22" viewBox="0 0 28 22"><ellipse cx="14" cy="12" rx="10" ry="7" fill="none" stroke="#fff" stroke-width="1.5"/><path d="M9 18v3M19 18v3M4 11H1" stroke="#fff" stroke-width="1.5"/></svg>
</div>

<section class="video" role="img" aria-label="Video still: a smiling woman holding a piggy bank, with a teal overlay">
  <div class="play">
    <svg width="62" height="62" viewBox="0 0 62 62"><path d="M26 20l14 11-14 11z" fill="#fff"/></svg>
  </div>
</section>

<section class="benefits">
  <div class="benefit" style="left:22px">
    <div class="art" role="img" aria-label="Illustration of stacked books and a graduation cap"></div>
    <div class="label">EDUCATION OF KIDS</div>
  </div>
  <div class="dash" style="left:145px"></div>
  <div class="benefit" style="left:212px">
    <div class="art" role="img" aria-label="Illustration of a cuckoo clock with coins"></div>
    <div class="label">PASSIVE INCOME</div>
  </div>
  <div class="dash" style="left:336px"></div>
  <div class="benefit" style="left:406px">
    <div class="art" role="img" aria-label="Illustration of a retired golfer swinging a club"></div>
    <div class="label">HAPPY RETIREMENT</div>
  </div>
</section>

<section class="calculator">
  <h2 class="calc-title">
    <span class="badge">
      <svg width="14" height="17" viewBox="0 0 14 17"><rect x="1" y="1" width="12" height="15" rx="1.5" fill="none" stroke="#fff" stroke-width="1.4"/><rect x="3.5" y="3.5" width="7" height="3" fill="#fff"/><path d="M4 9h1.5M8.5 9H10M4 12h1.5M8.5 12H10" stroke="#fff" stroke-width="1.5"/></svg>
    </span>
    Our online calculator
  </h2>

  <div class="field" style="top:173px">
    <svg width="42" height="40" viewBox="0 0 42 40" fill="none" stroke="#e8583a" stroke-width="1.5"><rect x="2" y="5" width="32" height="28" rx="2"/><path d="M2 12h32M9 1v7M27 1v7M8 18h3M15 18h3M22 18h3M8 24h3M15 24h3"/><circle cx="33" cy="31" r="7.5" fill="#fff"/><path d="M35 28h-3a1.5 1.5 0 000 3h2a1.5 1.5 0 010 3h-3M33 26v10"/></svg>
    Regular Monthly Investment:
  </div>

  <div class="range-label">Length of Investment</div>
  <div class="range">
    <div class="value">0</div>
    <svg width="430" height="30" viewBox="0 0 430 30" style="position:absolute;left:0;top:16px">
      <rect x="6" y="5" width="424" height="4" fill="#7d7d7d"/>
      <g stroke="#555" stroke-width="1">
        <path d="M6 10v4M25 10v3M44 10v3M63 10v3M82 10v3M100 10v5M119 10v3M138 10v3M157 10v3M176 10v3M194 10v5M213 10v3M232 10v3M251 10v3M270 10v3M288 10v5M307 10v3M326 10v3M345 10v3M364 10v3M382 10v5M401 10v3M420 10v3"/>
      </g>
      <circle cx="7" cy="7" r="6" fill="#e8583a"/><circle cx="7" cy="7" r="2.5" fill="#fff"/>
    </svg>
    <div class="ends" style="left:3px">0</div>
    <div class="ends" style="right:-3px">30 yrs</div>
  </div>

  <div class="field" style="top:317px">
    <svg width="42" height="40" viewBox="0 0 42 40" fill="none" stroke="#e8583a" stroke-width="1.5"><circle cx="22" cy="11" r="8.5"/><path d="M24.5 8h-3a1.5 1.5 0 000 3h1.5a1.5 1.5 0 010 3h-3M22.5 6v10"/><path d="M4 26l6-3c3-1 6 0 9 1h6a2 2 0 010 4h-7M4 34l5-2 10 2 13-7a2 2 0 00-2-3l-7 3"/></svg>
    One Time Payout:
  </div>

  <div class="field" style="top:380px">
    <svg width="42" height="40" viewBox="0 0 42 40" fill="none" stroke="#e8583a" stroke-width="1.5"><rect x="2" y="5" width="30" height="28" rx="2"/><path d="M2 12h30M9 1v7M25 1v7M8 18h18M8 24h12M14 14v16M20 14v16"/><circle cx="32" cy="31" r="7.5" fill="#e8583a"/><path d="M34 28h-3a1.5 1.5 0 000 3h2a1.5 1.5 0 010 3h-3M32 26v10" stroke="#fff"/></svg>
    Monthly Payment
  </div>

  <a class="invest-btn" href="#">
    I WANT TO INVEST
    <svg width="22" height="22" viewBox="0 0 22 22"><circle cx="11" cy="11" r="10" fill="#fff"/><path d="M9 6.5l4.5 4.5L9 15.5" fill="none" stroke="#e8583a" stroke-width="2.6"/></svg>
  </a>
</section>

<nav class="footer-nav">
  <a href="#">About Us</a>
  <a href="#">FAQ</a>
  <a href="#">Privacy Policy</a>
  <a href="#">Contact</a>
</nav>

</body>
</html>
```